Gaphic explaining connectivity of research areas that use DNA analysis

We are a university research group in Perth Western Australia focused on ecology and environment fields. Our work can be explained by three broad areas where its applied - what used to be present ('ancient DNA analysis'), what is present now ('environmental DNA analysis') and what happened in terms of DNA based changes in between ('genomic changes'). To help simply convey this to other researchers and importantly non-science-savvy people we wanted an a eye catching rework of the attached for our website, future presentations, brochures etc. We didn't want it too visually complicated, nor wordy so something akin to the attached with a better look will help . More background on each point can be read on the website under construction here - https://sciweb.halvorne.edu.au/quill-lab/

Target Market(s)

other science researchers in ecology, environment, geology, forensics areas, although ultimately its meant to be a simple way to understand for all people

Font styles to use
Sans Serif

Requirements
Must have
• the three areas indicated
Should not have
• design does not need to follow the colour pallet of the university (ie poo brown and black)

```html
<!DOCTYPE html>
<html lang="en">
<head>
<meta charset="utf-8">
<title>DNA Research Areas – Connectivity</title>
<link rel="stylesheet" href="https://fonts.googleapis.com/css2?family=Source+Sans+3:wght@600;700;800&display=swap">
<style>
  :root {
    --bg: #ffffff;
    --blue-light: #2a7fcb;
    --blue-mid: #1b63ae;
    --blue-dark: #134c91;
    --ring-edge: #0f3f7c;
    --yellow: #fcc010;
    --yellow-edge: #e7a800;
    --navy: #123f85;
    --ink: #111111;
  }
  html, body {
    margin: 0;
    padding: 0;
    width: 1200px;
    height: 1024px;
    overflow: hidden;
    background: var(--bg);
  }
  .canvas {
    width: 1200px;
    height: 1024px;
    display: block;
  }
  .diagram text {
    font-family: "Source Sans 3", "Myriad Pro", Arial, sans-serif;
    text-anchor: middle;
  }
  .pill { fill: var(--yellow); }
  .pill-label { fill: var(--navy); font-size: 31px; font-weight: 700; }
  .question { fill: var(--ink); font-size: 22px; font-weight: 700; }
  .insight { fill: var(--navy); font-size: 22px; font-weight: 700; }
  .hole { fill: var(--bg); }
  .ring-edge { fill: none; stroke: var(--ring-edge); stroke-width: 4; opacity: .55; }
  .connector-dot { fill: var(--yellow); stroke: var(--yellow-edge); stroke-width: 1.5; }
  .connector-arrow { fill: none; stroke: var(--navy); stroke-width: 2.6; stroke-linecap: round; stroke-linejoin: round; }
</style>
</head>
<body>
<svg class="canvas diagram" viewBox="0 0 1200 1024" xmlns="http://www.w3.org/2000/svg" role="img"
     aria-label="Three connected research areas: eDNA, aDNA and Genomics giving insight on Australian biodiversity">
  <defs>
    <linearGradient id="bandGradient" x1="0" y1="0" x2="1" y2="0.4">
      <stop offset="0" stop-color="var(--blue-light)"/>
      <stop offset="0.5" stop-color="var(--blue-mid)"/>
      <stop offset="1" stop-color="var(--blue-dark)"/>
    </linearGradient>
  </defs>

  <!-- connected blue band -->
  <g class="band" fill="url(#bandGradient)">
    <circle cx="302" cy="658" r="132"/>
    <circle cx="578" cy="360" r="132"/>
    <circle cx="886" cy="658" r="132"/>
    <path d="M368 544 Q430 505 464 426 L692 426 Q726 505 788 544 L820 772 Q578 700 368 772 Z"/>
  </g>

  <!-- ring openings -->
  <g class="holes">
    <circle class="hole" cx="578" cy="640" r="150"/>
    <circle class="hole" cx="578" cy="360" r="102"/>
    <circle class="ring-edge" cx="578" cy="360" r="104"/>
    <circle class="hole" cx="302" cy="658" r="104"/>
    <circle class="ring-edge" cx="302" cy="658" r="106"/>
    <circle class="hole" cx="886" cy="658" r="104"/>
    <circle class="ring-edge" cx="886" cy="658" r="106"/>
  </g>

  <!-- connectors -->
  <g class="connector">
    <circle class="connector-dot" cx="444" cy="496" r="14"/>
    <path class="connector-arrow" d="M438 502 L450 490 M442 490 L450 490 L450 498"/>
  </g>
  <g class="connector">
    <circle class="connector-dot" cx="734" cy="506" r="14"/>
    <path class="connector-arrow" d="M728 500 L740 512 M740 504 L740 512 L732 512"/>
  </g>

  <!-- aDNA -->
  <g class="area area-adna">
    <rect class="pill" x="506" y="299" width="168" height="43" rx="21.5"/>
    <text class="pill-label" x="590" y="332">aDNA</text>
    <text class="question" x="590" y="390">What used to</text>
    <text class="question" x="590" y="414">be present?</text>
  </g>

  <!-- eDNA -->
  <g class="area area-edna">
    <rect class="pill" x="216" y="590" width="168" height="43" rx="21.5"/>
    <text class="pill-label" x="300" y="623">eDNA</text>
    <text class="question" x="302" y="680">What is</text>
    <text class="question" x="302" y="704">present?</text>
  </g>

  <!-- Genomics -->
  <g class="area area-genomics">
    <rect class="pill" x="792" y="595" width="178" height="43" rx="21.5"/>
    <text class="pill-label" x="881" y="628">Genomics</text>
    <text class="question" x="886" y="676">What happened</text>
    <text class="question" x="886" y="698">along the</text>
    <text class="question" x="886" y="720">way?</text>
  </g>

  <!-- central insight -->
  <g class="insight-block">
    <text class="insight" x="588" y="586">Insight on the formation,</text>
    <text class="insight" x="588" y="616">distribution, and</text>
    <text class="insight" x="588" y="646">resilience of Australian</text>
    <text class="insight" x="588" y="676">biodiversity</text>
  </g>
</svg>
</body>
</html>
```